brightpath Business Card

Already have the logo, but now need the business card design

Industry/Entity Type

Business Software

Contact Information for Business Card

web site will be brightpath.io / The card should have the person name / position / mobile / email / and company address

Colors

Designer to choose colors to be used in the design.

Requirements
Must have
• See business card details
• One side to have the brightpath logo
Nice to have
• If possible the 'O' from flow can be watermarked into the second side
• Try to fit in the words brightpath Business Solutions

```html
<!DOCTYPE html>
<html lang="en">
<head>
<meta charset="utf-8">
<title>brightpath Business Card</title>
<link rel="stylesheet" href="https://fonts.googleapis.com/css2?family=Questrial&family=Arimo:wght@400;700&display=swap">
<style>
  :root {
    --stage: #2b2b2b;
    --card-grey: #787878;
    --card-white: #ffffff;
    --ink-grey: #6f6f6f;
    --ink-dark: #555555;
    --accent-red: #e0241c;
    --divider: #f2a9a0;
    --on-grey: #ffffff;
  }
  * { margin: 0; padding: 0; box-sizing: border-box; }
  html, body { width: 1200px; height: 880px; overflow: hidden; }
  body {
    background: var(--stage);
    display: flex;
    align-items: center;
    justify-content: center;
    gap: 40px;
  }
  .card {
    width: 540px;
    height: 310px;
    border-radius: 22px;
    position: relative;
    overflow: hidden;
  }
  .card-front {
    background: var(--card-grey);
    display: flex;
    flex-direction: column;
    align-items: center;
    justify-content: center;
  }
  .brand-name {
    font-family: "Questrial", sans-serif;
    font-weight: 400;
    letter-spacing: -1px;
    line-height: 1;
  }
  .card-front .brand-name {
    color: var(--on-grey);
    font-size: 78px;
  }
  .front-web {
    margin-top: 14px;
    font-family: "Arimo", sans-serif;
    font-size: 13px;
    letter-spacing: 1.5px;
    color: var(--on-grey);
  }
  .card-back {
    background: var(--card-white);
  }
  .card-back .brand-name {
    position: absolute;
    left: 34px;
    top: 168px;
    color: var(--ink-grey);
    font-size: 50px;
  }
  .divider {
    position: absolute;
    left: 288px;
    top: 70px;
    width: 1px;
    height: 170px;
    background: linear-gradient(var(--card-white), var(--divider) 30%, var(--divider) 70%, var(--card-white));
  }
  .contact {
    position: absolute;
    left: 310px;
    top: 66px;
    font-family: "Arimo", sans-serif;
    color: var(--ink-dark);
  }
  .person-name { font-size: 17px; font-weight: 700; color: var(--ink-grey); }
  .person-role { font-size: 13px; color: var(--accent-red); margin-bottom: 10px; }
  .address { font-size: 12.5px; line-height: 1.4; margin-bottom: 10px; }
  .contact-list { list-style: none; font-size: 12.5px; }
  .contact-list li { display: flex; align-items: center; gap: 7px; margin-bottom: 4px; }
  .contact-icon { width: 16px; height: 16px; flex: none; }
  .web-domain { color: var(--accent-red); }
</style>
</head>
<body>
  <section class="card card-front">
    <div class="brand-name">brightpath</div>
    <div class="front-web">www.brightpath.io</div>
  </section>

  <section class="card card-back">
    <div class="brand-name">brightpath</div>
    <div class="divider"></div>
    <div class="contact">
      <div class="person-name">Daniel Reed</div>
      <div class="person-role">Founder</div>
      <div class="address">PO BOX 450 Harbour Lane<br>4th street Geelong</div>
      <ul class="contact-list">
        <li>
          <svg class="contact-icon" viewBox="0 0 16 16" aria-hidden="true">
            <circle cx="8" cy="8" r="7" fill="none" stroke="var(--accent-red)" stroke-width="1.5"/>
            <path d="M5.5 4.5l1.3-.3.8 1.8-.9.7a5 5 0 0 0 2.6 2.6l.7-.9 1.8.8-.3 1.3c-3.3.2-6.2-2.7-6-6z" fill="var(--accent-red)"/>
          </svg>
          <span>(555) 013-2468</span>
        </li>
        <li>
          <svg class="contact-icon" viewBox="0 0 16 16" aria-hidden="true">
            <circle cx="8" cy="8" r="7" fill="none" stroke="var(--accent-red)" stroke-width="1.5"/>
            <rect x="4.3" y="5.3" width="7.4" height="5.4" fill="var(--accent-red)"/>
            <path d="M4.3 5.3L8 8.3l3.7-3" fill="none" stroke="#fff" stroke-width="0.9"/>
          </svg>
          <span>info@brightpathmail.com</span>
        </li>
        <li>
          <svg class="contact-icon" viewBox="0 0 16 16" aria-hidden="true">
            <circle cx="8" cy="8" r="7" fill="none" stroke="var(--accent-red)" stroke-width="1.5"/>
            <circle cx="8" cy="8" r="4" fill="none" stroke="var(--accent-red)" stroke-width="1"/>
            <path d="M4 8h8M8 4v8M5 5.8h6M5 10.2h6" stroke="var(--accent-red)" stroke-width="0.8"/>
          </svg>
          <span>www.<span class="web-domain">brightpath.io</span></span>
        </li>
      </ul>
    </div>
  </section>
</body>
</html>
```